Atendimento nota 11, sem contar a agilidade das pessoas, nos apresentaram diversos modelos e formas de logo. Com certeza iremos indica-lo para outras pessoas.

```html
<!DOCTYPE html>
<html lang="pt-BR">
<head>
<meta charset="utf-8">
<title>Valore Imóveis – Placa de porta</title>
<link rel="stylesheet" href="https://fonts.googleapis.com/css2?family=Arimo:wght@400&display=swap">
<style>
  :root {
    --backdrop: #ebebea;
    --plaque-brown: #2f1f14;
    --gold-light: #f1e2a6;
    --gold-mid: #c9ad62;
    --gold-deep: #9c8140;
    --text-light: #e6e1da;
  }
  * { box-sizing: border-box; margin: 0; padding: 0; }
  html, body {
    width: 1200px;
    height: 1200px;
    overflow: hidden;
    background: var(--backdrop);
  }
  .canvas {
    position: relative;
    width: 1200px;
    height: 1200px;
  }
  .plaque {
    position: absolute;
    left: 173px;
    top: 492px;
    width: 832px;
    height: 216px;
    background: var(--plaque-brown);
    border-radius: 6px 0 0 6px;
  }
  .plaque-edge {
    position: absolute;
    left: 998px;
    top: 486px;
    width: 28px;
    height: 222px;
    background: linear-gradient(90deg, var(--gold-deep) 0%, var(--gold-light) 45%, var(--gold-mid) 100%);
    border-radius: 0 4px 4px 0;
  }
  .brand {
    position: absolute;
    left: 215px;
    top: 524px;
    width: 320px;
    display: flex;
    flex-direction: column;
    align-items: center;
    gap: 22px;
    font-family: "Arimo", sans-serif;
    font-weight: 400;
    font-size: 30px;
    letter-spacing: 2px;
    color: var(--gold-mid);
    text-transform: uppercase;
    white-space: nowrap;
  }
  .brand-square {
    width: 56px;
    height: 56px;
    background: var(--gold-mid);
    flex: none;
  }
  .divider {
    position: absolute;
    left: 566px;
    top: 530px;
    width: 2px;
    height: 138px;
    background: var(--gold-mid);
  }
  .contact {
    position: absolute;
    left: 590px;
    top: 564px;
    width: 382px;
    font-family: "Arimo", sans-serif;
    font-size: 15.5px;
    line-height: 24px;
    color: var(--text-light);
    list-style: none;
    text-align: right;
    white-space: nowrap;
  }
</style>
</head>
<body>
  <main class="canvas">
    <div class="plaque"></div>
    <div class="plaque-edge"></div>

    <div class="brand">
      <span class="brand-square"></span>
      <span class="brand-name">Valore Imóveis</span>
    </div>

    <div class="divider"></div>

    <ul class="contact">
      <li class="contact-address">Rua 118, nº 45, Sala 03 Porto Belo - Centro - SC</li>
      <li class="contact-postcode">CEP: 88210-000</li>
      <li class="contact-phone">(47) 3295-0418</li>
    </ul>
  </main>
</body>
</html>
```